Biodegradable box for eco-friendly bamboo cotton buds

I am looking for a design on a box holding 200 bamboo cotton buds. The box opens like a matchstick box and is made from recycled card. It's to sell online and at markets, maybe also supermarkets.
It's the second product my company, LeafMarta, will sell, so I would like a design that I can replicate on other product packaging in the future.
You can see more about LeafMarta on my website www.leafmarta.org or facebook and instagram @leafmartaqatar.
Please see below the box dimensions from the supplier and a photo. Also, some ideas I have had using Canva. I would like to see the green strip go all the way round the box. I like the font. The cotton bud logo is copyrighted - I like the style, but a new one would need to be created.

Target Market(s)

Eco-conscious consumers - expats and locals - in Qatar

Industry/Entity Type

Retail

Font styles to use
Other font styles liked:
• special elite

Colors
cadf82
acd037
eaf2ce
9ccb3b

Requirements
Must have
• an environmentally-friendly focus

```html
<!DOCTYPE html>
<html lang="en">
<head>
<meta charset="UTF-8">
<title>LeafMarta — Bamboo Cotton Buds Box Front</title>
<link rel="stylesheet" href="https://fonts.googleapis.com/css2?family=Special+Elite&family=Nunito:wght@400&display=swap">
<style>
  :root {
    --cream: #eaf2ce;
    --cream-soft: #e3ebcb;
    --leaf: #acd037;
    --leaf-mid: #9ccb3b;
    --pale-green: #cadf82;
    --ink: #1a1a1a;
    --backdrop: #eeeeee;
  }
  * { margin: 0; padding: 0; box-sizing: border-box; }
  html, body {
    width: 1200px;
    height: 900px;
    overflow: hidden;
    background: var(--backdrop);
  }
  .canvas {
    width: 1200px;
    height: 900px;
    display: flex;
    align-items: center;
    justify-content: center;
  }
  .box-front {
    position: relative;
    width: 580px;
    height: 740px;
    display: flex;
    background: var(--cream-soft);
  }
  .label-panel {
    position: relative;
    width: 414px;
    height: 100%;
    background: linear-gradient(180deg, var(--cream) 0%, var(--cream-soft) 100%);
  }
  .product-title {
    position: absolute;
    top: 62px;
    right: 30px;
    text-align: right;
    font-family: "Special Elite", "Courier New", monospace;
    font-weight: 400;
    color: var(--ink);
    line-height: 1;
  }
  .product-title .title-main {
    display: block;
    font-size: 90px;
  }
  .product-title .title-sub {
    display: block;
    font-size: 50px;
    margin-top: 2px;
  }
  .bud-illustration {
    position: absolute;
    left: 50px;
    top: 262px;
    width: 364px;
    height: 340px;
    background: var(--pale-green);
    opacity: 0.5;
    border-radius: 24px;
  }
  .count-tag {
    position: absolute;
    left: 0;
    top: 628px;
    width: 176px;
    height: 76px;
    background: var(--leaf);
    border-radius: 0 6px 6px 0;
    display: flex;
    align-items: center;
    justify-content: center;
    font-family: "Special Elite", "Courier New", monospace;
    font-size: 44px;
    color: var(--ink);
  }
  .count-tag .unit { font-size: 32px; }
  .brand-strip {
    position: relative;
    flex: 1;
    height: 100%;
    background: var(--leaf);
  }
  .strip-mark {
    position: absolute;
    top: 74px;
    left: 50%;
    transform: translateX(-50%);
    width: 96px;
    height: 96px;
    border-radius: 50%;
    background: var(--pale-green);
    opacity: 0.6;
  }
  .brand-lockup {
    position: absolute;
    left: 0;
    right: 0;
    top: 560px;
    text-align: center;
    font-family: "Nunito", sans-serif;
    color: var(--ink);
  }
  .brand-dot {
    display: block;
    width: 30px;
    height: 30px;
    margin: 0 auto 20px;
    border-radius: 50%;
    border: 2px solid var(--ink);
  }
  .brand-name {
    display: block;
    font-size: 28px;
    line-height: 1.1;
  }
  .brand-tagline {
    display: block;
    font-size: 14px;
    margin-top: 4px;
    text-align: right;
    padding-right: 18px;
  }
</style>
</head>
<body>
  <main class="canvas">
    <section class="box-front">
      <div class="label-panel">
        <h1 class="product-title">
          <span class="title-main">bamboo</span>
          <span class="title-sub">cotton buds</span>
        </h1>
        <div class="bud-illustration" role="img" aria-label="Line illustration of two crossed cotton buds in pale green"></div>
        <div class="count-tag">200<span class="unit">ea</span></div>
      </div>
      <aside class="brand-strip">
        <div class="strip-mark"></div>
        <div class="brand-lockup">
          <span class="brand-dot"></span>
          <span class="brand-name">LeafMarta</span>
          <span class="brand-tagline">Tread gently</span>
        </div>
      </aside>
    </section>
  </main>
</body>
</html>
```